International Biotech Startup needs a professionally looking web Design

We need a web design for a small biotech company based in Singapore which has global Pharma and Biotech Customers.

Our current website: www.zelvintralabs.com

However this was generated by few of us. We would require a professional design for biotech companies like us. The appearance of the website should be appealing to users and this is mainly a promotional website without any financial transactions.
Once the design is approved, we will provide the updated text.

Target Market(s)

Pharmaceutical, Biotech, healthcare

Industry/Entity Type

Biotechnology

Coding

Coded - Design and coding required

Number of Pages Required

5+ page

Requirements
Must have
• the website needs favicon.
Nice to have
• Please some of the companies websites that we like the most or they are in the similar domain. We would like to have something like that:
• http://www.pinecrestgenomics.com/
• http://www.marlowtherapeutics.com/
• http://www.tendrix.com/
• http://www.velunar.com/
• www.dornavil.com

```html
<!DOCTYPE html>
<html lang="en">
<head>
<meta charset="utf-8">
<title>Zelvintra Labs</title>
<link href="https://fonts.googleapis.com/css2?family=Raleway:wght@400;500;600&family=Open+Sans:wght@400;600&display=swap" rel="stylesheet">
<style>
:root{
  --navy:#2f5c93;
  --navy-dark:#234a7a;
  --yellow:#f5b800;
  --ink:#2b2b2b;
  --body:#555;
  --panel:#efefef;
  --white:#fff;
}
*{margin:0;padding:0;box-sizing:border-box}
html,body{width:1200px;height:2821px;overflow:hidden;background:var(--white)}
body{position:relative;font-family:"Open Sans",sans-serif;color:var(--body)}
.abs{position:absolute}
h1,h2,h3,.nav a{font-family:"Raleway",sans-serif;font-weight:400}

/* hero */
.hero{left:0;top:0;width:1200px;height:660px;background:linear-gradient(100deg,#6f8e9e 0%,#a9c2cc 35%,#dbe6ea 60%,#c9d7de 100%)}
.brand-mark{left:0;top:110px;width:1200px;text-align:center;font-family:"Raleway",sans-serif;font-weight:600;font-size:88px;color:var(--navy);letter-spacing:1px}
.welcome{left:0;top:360px;width:1200px;text-align:center;font-size:60px;color:var(--navy);letter-spacing:2px}
.welcome-rule{top:398px;height:2px;width:190px;background:var(--yellow)}
.tagline{left:0;top:465px;width:1200px;text-align:center;font-family:"Raleway",sans-serif;font-size:48px;color:#222}
.tagline span{color:var(--yellow)}
.nav{left:0;top:598px;width:1200px;height:60px;background:rgba(255,255,255,.55);border-top:2px solid var(--yellow)}
.nav a{position:absolute;top:0;height:58px;line-height:58px;font-size:18px;color:#222;text-decoration:none;transform:translateX(-50%)}
.nav a.active{background:var(--navy);color:var(--yellow);width:105px;text-align:center}
.band{left:0;height:8px;width:1200px;background:var(--yellow)}
.pointer{width:0;height:0;border-left:14px solid transparent;border-right:14px solid transparent;border-top:14px solid var(--yellow)}
.shade{height:30px;background:radial-gradient(ellipse at top,rgba(0,0,0,.25),rgba(0,0,0,0) 70%)}

/* about */
.section-title{font-size:42px;color:var(--navy)}
.title-rule{height:2px;background:var(--yellow)}
.about-text{left:79px;top:800px;width:520px;font-size:13.5px;line-height:23px;color:#555}
.btn{left:77px;top:1044px;width:146px;height:51px;background:var(--yellow);border:1px solid #d79b00;border-radius:3px;color:#333;font-size:16px;line-height:49px;text-align:center}
.product-visual{left:724px;top:715px;width:282px;height:385px;border-radius:40% 40% 30% 30%;background:radial-gradient(ellipse at 40% 70%,#2f5c93 0%,#9fb0c4 45%,#fff 75%)}

/* press */
.press{left:77px;top:1147px;width:1046px;height:236px;background:var(--panel);border-bottom:4px solid var(--yellow)}
.badge{position:absolute;width:200px;height:54px;background:#d7d9dd;border-radius:4px}

/* features */
.feature{width:480px;text-align:center}
.feature-icon{position:absolute;left:161px;top:0;width:158px;height:158px;border-radius:50%;background:var(--navy)}
.feature h3{position:absolute;top:168px;width:100%;font-size:40px;color:var(--navy)}
.feature p{position:absolute;top:235px;left:55px;width:370px;font-size:15px;line-height:25px;color:#555}
.divider{left:598px;top:1486px;width:1px;height:339px;background:#ccc}

/* contact */
.contact{left:0;top:1900px;width:1200px;height:621px;background:radial-gradient(circle at 20% 70%,#4f8bc8 0%,#2a5d94 45%,#1e4f86 100%)}
.contact-title{left:0;top:1943px;width:1200px;text-align:center;font-size:40px;color:var(--yellow)}
.contact-lead{left:280px;top:2010px;width:640px;text-align:center;font-size:12.5px;line-height:22px;color:#fff}
.sub-title{font-size:24px;color:var(--yellow);text-align:center}
.field{background:rgba(80,130,190,.6);border:1px solid #7fa6d3;color:#fff;font-size:12.5px;padding:8px 12px}
.send{left:129px;top:2345px;width:106px;height:106px;border-radius:50%;background:rgba(120,160,210,.7);border:3px solid #6fa0d6}
.send-inner{position:absolute;left:14px;top:14px;width:72px;height:72px;border-radius:50%;border:5px solid #111;background:#4a7fbd}
.map{left:856px;top:2211px;width:206px;height:206px;border-radius:50%;border:3px solid var(--yellow);background:radial-gradient(circle at 45% 40%,#f2c52a,#2a5d94 75%)}
.address{left:867px;top:2304px;width:220px;height:141px;background:rgba(47,92,147,.8);border:1px solid #7fa6d3;color:#fff;text-align:center;font-size:13.5px;line-height:23px;padding-top:10px}
.address strong{font-size:16px}

/* footer */
.top-link{left:562px;top:2552px;width:76px;height:76px;border-radius:50%;border:4px solid var(--navy)}
.copyright{left:0;top:2646px;width:1200px;text-align:center;font-size:14px;color:#333}
.copyright span{color:var(--navy)}
.social{top:2686px;width:56px;height:56px;border-radius:50%;background:#b9b9b9;border:3px solid #ddd}
.social.first{background:var(--navy)}
.footer-bar{left:0;top:2799px;width:1200px;height:22px;background:var(--navy);border-top:4px solid var(--yellow)}
</style>
</head>
<body>

<header>
  <div class="abs hero" role="img" aria-label="Laboratory photograph of a scientist with a pipette and server racks, blue tone"></div>
  <div class="abs brand-mark">Zelvintra Labs</div>
  <div class="abs welcome-rule" style="left:252px"></div>
  <div class="abs welcome-rule" style="left:778px"></div>
  <h1 class="abs welcome">WELCOME</h1>
  <h2 class="abs tagline">To The <span>Zelvintra Labs</span></h2>
  <nav class="abs nav">
    <a class="active" href="#" style="left:241px">HOME</a>
    <a href="#" style="left:354px">ABOUT</a>
    <a href="#" style="left:502px">TECHNOLOGY</a>
    <a href="#" style="left:670px">PRODUCTS</a>
    <a href="#" style="left:800px">NEWS</a>
    <a href="#" style="left:931px">CONTACTS</a>
  </nav>
  <div class="abs band" style="top:658px"></div>
  <div class="abs pointer" style="left:586px;top:666px"></div>
  <div class="abs shade" style="left:80px;top:666px;width:1040px"></div>
</header>

<section class="about">
  <h2 class="abs section-title" style="left:79px;top:722px">About</h2>
  <div class="abs title-rule" style="left:226px;top:752px;width:176px"></div>
  <p class="abs about-text">Zelvintra Labs is a Singapore-based synthetic biology company. We specialize in providing customized membrane protein products, services and expertise for drug discovery, diagnostics, and biomedical applications. Our company is backed by an international team of scientists, with diverse interdisciplinary backgrounds in synthetic chemistry, materials science, nanotechnology, cell signaling, and immunology. Our business team has extensive experience in biotechnology with a proven track record of working with small and big biotech and pharma companies all over the world.</p>
  <div class="abs btn">READ MORE</div>
  <div class="abs product-visual" role="img" aria-label="Illustration of an open blue and white capsule releasing a molecular structure"></div>
</section>

<section class="abs press" aria-label="Featured in">
  <div class="badge" style="left:28px;top:38px"></div>
  <div class="badge" style="left:290px;top:38px"></div>
  <div class="badge" style="left:552px;top:38px"></div>
  <div class="badge" style="left:814px;top:38px"></div>
  <div class="badge" style="left:28px;top:134px"></div>
  <div class="badge" style="left:290px;top:134px"></div>
  <div class="badge" style="left:552px;top:134px"></div>
  <div class="badge" style="left:814px;top:134px"></div>
</section>
<div class="abs pointer" style="left:586px;top:1383px"></div>
<div class="abs shade" style="left:80px;top:1387px;width:1040px"></div>

<section>
  <div class="abs feature" style="left:89px;top:1458px">
    <div class="feature-icon">
      <svg width="158" height="158" viewBox="0 0 158 158" fill="none" stroke="#fff" stroke-width="5">
        <ellipse cx="79" cy="79" rx="44" ry="17"/>
        <ellipse cx="79" cy="79" rx="44" ry="17" transform="rotate(60 79 79)"/>
        <ellipse cx="79" cy="79" rx="44" ry="17" transform="rotate(-60 79 79)"/>
        <circle cx="79" cy="79" r="7" fill="#fff"/>
      </svg>
    </div>
    <h3>Technology</h3>
    <p>The synthetic membrane platform (ZMP) is a proprietary technology which is used to provide high-quality functional membrane proteins (drug targets, for example) in a native-like environment using engineered polymer membranes, without the use of cells.</p>
  </div>
  <div class="abs divider"></div>
  <div class="abs feature" style="left:625px;top:1458px">
    <div class="feature-icon">
      <svg width="158" height="158" viewBox="0 0 158 158" fill="none" stroke="#fff" stroke-width="5" stroke-linejoin="round">
        <path d="M44 62 L79 46 L114 62 L114 100 L79 116 L44 100 Z"/>
        <path d="M44 62 L79 78 L114 62 M79 78 L79 116"/>
      </svg>
    </div>
    <h3>Products</h3>
    <p>In addition to partnering with our clients in key areas of drug discovery, Zelvintra Labs also provides high-quality products per request for interested customers. Please let us know your needs via the Contact page, and our scientists will get back to you with more details.</p>
  </div>
</section>

<section>
  <div class="abs contact" role="img" aria-label="Blue background of microscopic cells joined by network lines"></div>
  <div class="abs title-rule" style="left:290px;top:1971px;width:180px"></div>
  <div class="abs title-rule" style="left:730px;top:1971px;width:180px"></div>
  <h2 class="abs contact-title">Contact Us</h2>
  <p class="abs contact-lead">Lorem Ipsum is simply dummy text of the printing and typesetting industry. Lorem Ipsum has been the industry's standard dummy text ever since the 1500s, when an unknown printer took a galley of type and scrambled it to make a type.</p>

  <div class="abs title-rule" style="left:113px;top:2141px;width:180px"></div>
  <div class="abs title-rule" style="left:560px;top:2141px;width:174px"></div>
  <h3 class="abs sub-title" style="left:293px;top:2125px;width:267px">Send Us a Message</h3>
  <form>
    <div class="abs field" style="left:77px;top:2191px;width:218px;height:42px">Name</div>
    <div class="abs field" style="left:316px;top:2191px;width:218px;height:42px">E-Mail</div>
    <div class="abs field" style="left:557px;top:2191px;width:216px;height:42px">Subject</div>
    <div class="abs field" style="left:77px;top:2254px;width:696px;height:144px">Message</div>
    <div class="abs send"><div class="send-inner">
      <svg width="62" height="62" viewBox="0 0 62 62" fill="none" stroke="#fff" stroke-width="3"><rect x="16" y="20" width="30" height="22"/><path d="M16 20 L31 33 L46 20"/></svg>
    </div></div>
  </form>

  <h3 class="abs sub-title" style="left:830px;top:2125px;width:250px">CONTACT INFO</h3>
  <div class="abs map" role="img" aria-label="Map of Southeast Asia highlighting Singapore"></div>
  <svg class="abs" style="left:890px;top:2235px" width="36" height="50" viewBox="0 0 36 50"><path d="M18 48 C6 30 2 24 2 17 A16 16 0 0 1 34 17 C34 24 30 30 18 48Z" fill="#e03a6c"/><circle cx="18" cy="17" r="6" fill="#fff"/></svg>
  <address class="abs address" style="font-style:normal"><strong>Zelvintra Labs Pte Ltd.</strong><br>18 Kestrel Link,<br>Meridian Science Hub,<br>Level 4, Singapore 648210</address>
</section>

<footer>
  <div class="abs top-link">
    <svg width="68" height="68" viewBox="0 0 68 68"><path d="M20 42 L34 24 L48 42 L34 36 Z" fill="#2f5c93"/></svg>
  </div>
  <p class="abs copyright">© <span>Zelvintra Labs</span> 2015. All Rights Reserved</p>
  <div class="abs social first" style="left:463px"></div>
  <div class="abs social" style="left:536px"></div>
  <div class="abs social" style="left:610px"></div>
  <div class="abs social" style="left:683px"></div>
  <div class="abs pointer" style="left:586px;top:2785px;border-top:0;border-bottom:14px solid var(--yellow)"></div>
  <div class="abs footer-bar"></div>
</footer>

</body>
</html>
```